Ecommerce Website For Printing Company

Zoravquill.com are a print, design and signage company who sell flyers, business cards, posters, brochures and more to customers in the UK.

Our website is outdated and requires a new design using current web styling and mobile functionality.

We require the following pages to be designed;
- Home Page
- Price Page
- Portfolio Page
- Blog
- Content Page

Our competitors in the printing industry are www.brenticade.com, www.hallowmarsh.co.uk, quorelvane.co.uk, www.tambridok.co.uk

We require the website to give a professional image as well as be easy for customers to navigate, understand and find prices.

Target Market(s)

Businesses

Industry/Entity Type

Printing

Number of Pages Required

4 page

Font styles to use
Sans Serif

Colors
33a6d7

Requirements
Must have
• Popular products, latest news/blog, sales from portfolio, newsletter sign up, footer

```html
<!DOCTYPE html>
<html lang="en">
<head>
<meta charset="utf-8">
<title>Zoravquill.com – Print, Signage, Websites, Design</title>
<link rel="stylesheet" href="https://fonts.googleapis.com/css2?family=Open+Sans:ital,wght@0,400;0,600;0,700;1,400&family=Oswald:wght@400;500;600&family=Kaushan+Script&display=swap">
<style>
:root{
  --brand:#33a6d7;
  --brand-dark:#1f86b8;
  --ink:#2d3339;
  --topbar:#3a3f44;
  --grey-bg:#e9ebed;
  --card:#ffffff;
  --muted:#8a9096;
  --orange:#f07d1a;
  --footer:#24282c;
  --footer-deep:#16191c;
}
*{box-sizing:border-box;margin:0;padding:0}
html,body{width:1200px;height:2800px;overflow:hidden}
body{font-family:"Open Sans",Arial,sans-serif;color:var(--ink);background:#fff;position:relative}
a{color:inherit;text-decoration:none}

/* top utility bar */
.utility-bar{height:28px;background:var(--topbar);color:#d6dade;font-size:12px;display:flex;align-items:center;justify-content:space-between;padding:0 80px}
.utility-bar nav{display:flex;gap:26px;margin-left:260px}
.utility-bar .account{display:flex;gap:24px}
.utility-bar span{display:flex;align-items:center;gap:6px}
.utility-bar svg{width:11px;height:11px;fill:var(--brand)}

/* header */
.site-header{height:112px;display:flex;align-items:center;justify-content:space-between;padding:0 80px}
.brand{display:flex;align-items:center;gap:12px}
.brand-mark{width:22px;height:22px;background:var(--brand)}
.brand-name{font-family:"Oswald",sans-serif;font-weight:500;font-size:40px;color:var(--brand);letter-spacing:.5px}
.header-phone{display:flex;align-items:center;gap:12px;font-family:"Oswald",sans-serif;font-size:40px;color:var(--brand)}
.header-phone svg{width:34px;height:34px;fill:var(--brand)}

/* main nav */
.main-nav{height:42px;background:var(--brand);display:flex;padding:0 80px}
.main-nav a{color:#fff;font-size:14px;font-weight:600;text-transform:uppercase;padding:0 21px;display:flex;align-items:center}
.main-nav a.active{background:var(--brand-dark)}

/* hero */
.hero{position:relative;height:558px;background:linear-gradient(120deg,#cfd2d5 0%,#e7e8ea 45%,#dadcde 100%)}
.hero-art{position:absolute;left:80px;top:40px;width:520px;height:480px;background:linear-gradient(160deg,#f4f4f4,#c9ccd0);border-radius:2px}
.hero-copy{position:absolute;left:690px;top:170px;width:440px}
.hero-copy h1{font-family:"Oswald",sans-serif;font-weight:600;font-size:68px;line-height:1;color:#1c2024;letter-spacing:1px}
.hero-copy p{font-style:italic;font-size:17px;color:#3a3f44;margin-top:14px}
.price-badge{position:absolute;left:800px;top:400px;width:150px;height:150px;border-radius:50%;background:var(--brand);color:#fff;display:flex;flex-direction:column;align-items:center;justify-content:center;box-shadow:0 0 0 6px rgba(255,255,255,.55)}
.price-badge small{font-size:17px}
.price-badge strong{font-family:"Oswald",sans-serif;font-weight:500;font-size:56px;line-height:1}

/* promo strip */
.promo-strip{height:200px;background:var(--grey-bg);display:flex;gap:40px;padding:40px 80px}
.promo{flex:1;height:120px;position:relative;overflow:hidden}
.promo-delivery{background:linear-gradient(90deg,var(--brand),#58bde6);color:#fff;padding:34px 40px}
.promo-delivery h2{font-family:"Oswald",sans-serif;font-weight:500;font-size:38px;line-height:1}
.promo-delivery p{font-size:14px;margin-top:6px}
.promo-delivery .van{position:absolute;right:30px;top:22px;width:180px;height:78px;background:linear-gradient(90deg,#e9f6fc,#bfe4f4);border-radius:4px}
.promo-cards{background:#2a2f34;color:#fff}
.promo-cards .card-art{position:absolute;left:0;top:0;width:190px;height:120px;background:linear-gradient(135deg,#55606a,#8b949c)}
.promo-cards .card-copy{position:absolute;left:220px;top:18px}
.promo-cards .card-copy h3{font-size:15px;font-weight:400;background:#fff;color:var(--ink);padding:3px 10px;display:inline-block}
.promo-cards .card-copy h3 b{color:var(--brand)}
.promo-cards .card-copy p{font-size:12px;margin-top:6px;color:#cfd3d7}
.btn-order{display:inline-block;margin-top:12px;background:#111;border:1px solid #666;color:#fff;font-size:13px;font-weight:700;padding:7px 16px}

/* popular products */
.popular{height:540px;display:flex;background:var(--grey-bg)}
.category-list{width:330px;background:var(--brand);color:#fff}
.category-list h2{font-family:"Oswald",sans-serif;font-weight:500;font-size:24px;background:var(--brand-dark);padding:10px 20px;text-transform:uppercase}
.category-list ul{list-style:none;padding:8px 0}
.category-list li{font-size:14px;padding:9px 20px 9px 36px;position:relative;border-bottom:1px solid rgba(255,255,255,.15)}
.category-list li::before{content:"";position:absolute;left:20px;top:15px;border:4px solid transparent;border-left-color:#fff}
.category-list li.current{background:#fff;color:var(--brand);font-weight:600}
.category-list li.current::before{border-left-color:var(--brand)}
.product-grid{flex:1;display:grid;grid-template-columns:repeat(3,240px);gap:30px 36px;padding:36px 0 0 40px;align-content:start}
.product-card{background:var(--card);height:212px;padding:12px;box-shadow:0 1px 3px rgba(0,0,0,.1)}
.product-image{height:124px;background:linear-gradient(135deg,#7a8a6a,#c9c2a8)}
.product-card:nth-child(3n+1) .product-image{background:linear-gradient(135deg,#c4cbd2,#f1f2f3)}
.product-card h3{font-size:13px;font-weight:600;margin-top:10px}
.product-meta{display:flex;justify-content:space-between;align-items:center;margin-top:6px;font-size:13px;color:var(--muted)}
.btn-shop{background:var(--brand);color:#fff;font-size:11px;font-weight:700;padding:5px 10px}

/* portfolio */
.portfolio{height:420px;padding-top:40px;text-align:center;position:relative}
.section-title{font-family:"Oswald",sans-serif;font-weight:400;font-size:26px;color:var(--brand);text-transform:uppercase;letter-spacing:1px}
.portfolio-row{display:flex;justify-content:center;gap:56px;margin-top:40px}
.portfolio-item{width:220px}
.portfolio-image{height:190px;background:linear-gradient(150deg,#e3e6e8,#8fb0c2)}
.portfolio-item:nth-child(3) .portfolio-image{background:linear-gradient(150deg,#7d9b52,#d4d9c6)}
.portfolio-item h3{font-size:17px;font-weight:600;margin-top:18px}
.carousel-arrow{position:absolute;top:200px;width:20px;height:40px}
.carousel-arrow path{fill:none;stroke:var(--brand);stroke-width:4}
.carousel-arrow.prev{left:40px}.carousel-arrow.next{right:40px}

/* blog */
.latest-news{height:430px;background:var(--grey-bg);display:flex;padding:40px 80px;gap:60px}
.news-image{width:440px;height:350px;background:linear-gradient(140deg,#eff1f2,#7ea04f 60%,#2f3a27)}
.news-body{width:500px;padding-top:20px}
.news-body h2{font-family:"Oswald",sans-serif;font-weight:400;font-size:30px;color:var(--brand)}
.news-meta{font-size:11px;color:var(--muted);margin-top:4px}
.news-body p{font-size:13px;line-height:1.65;color:#555b61;margin-top:18px}
.read-more{display:block;font-size:12px;font-weight:700;color:var(--brand);margin-top:8px}
.btn-blog{display:inline-block;margin-top:18px;background:#1c2024;color:#fff;font-size:12px;font-weight:700;padding:9px 18px}

/* offer band */
.offer-band{height:110px;display:flex;background:#0d0f11;color:#fff}
.offer-label{width:440px;background:linear-gradient(90deg,var(--orange),#f5a03a);clip-path:polygon(0 0,100% 0,88% 100%,0 100%);display:flex;align-items:center;padding-left:70px;font-family:"Kaushan Script",cursive;font-size:50px}
.offer-detail{flex:1;position:relative}
.offer-detail .season{position:absolute;left:240px;top:12px;font-family:"Kaushan Script",cursive;font-size:24px;color:var(--orange)}
.offer-detail .deal{position:absolute;left:60px;top:50px;display:flex;align-items:center;gap:20px;font-family:"Oswald",sans-serif;font-size:40px;font-weight:500}
.offer-detail .deal i{width:3px;height:40px;background:#fff}

/* footer */
.site-footer{height:310px;background:var(--footer);color:#cfd3d7;display:flex;gap:80px;padding:40px 80px}
.site-footer h3{font-size:18px;font-weight:600;color:#fff;margin-bottom:18px}
.footer-links{width:300px}
.footer-links li{list-style:none;font-size:12px;margin-bottom:10px}
.footer-links li:first-child{color:var(--brand)}
.footer-contact{width:340px}
.contact-line{display:flex;gap:10px;font-size:12px;margin-bottom:12px;line-height:1.5}
.contact-line svg{flex:none;width:14px;height:14px;fill:var(--brand);margin-top:2px}
.payment-row{display:flex;flex-wrap:wrap;gap:10px;width:200px}
.payment-row span{width:44px;height:28px;background:#e6e8ea;border-radius:3px}
.legal-bar{height:50px;background:var(--footer-deep);color:#8a9096;font-size:11px;text-align:center;padding-top:10px;line-height:1.5}
</style>
</head>
<body>

<div class="utility-bar">
  <nav>
    <span><svg viewBox="0 0 10 10"><path d="M1 1h8v6H4l-3 2z"/></svg>TESTIMONIALS</span>
    <span><svg viewBox="0 0 10 10"><rect x="1" y="1" width="8" height="8"/></svg>BLOG</span>
    <span><svg viewBox="0 0 10 10"><path d="M1 2h8v6H1z"/></svg>CONTACT</span>
  </nav>
  <div class="account">
    <span><svg viewBox="0 0 10 10"><circle cx="5" cy="3" r="2.5"/><path d="M0 10a5 4 0 0 1 10 0z"/></svg>My Account</span>
    <span><svg viewBox="0 0 10 10"><path d="M0 1h2l1 6h6l1-4H3"/></svg>My Cart</span>
  </div>
</div>

<header class="site-header">
  <a class="brand" href="#"><span class="brand-mark"></span><span class="brand-name">Zoravquill.com</span></a>
  <div class="header-phone">
    <svg viewBox="0 0 24 24"><path d="M6.6 10.8a15 15 0 0 0 6.6 6.6l2.2-2.2a1 1 0 0 1 1-.25 11.4 11.4 0 0 0 3.6.57 1 1 0 0 1 1 1V20a1 1 0 0 1-1 1A17 17 0 0 1 3 4a1 1 0 0 1 1-1h3.5a1 1 0 0 1 1 1c0 1.25.2 2.45.57 3.57a1 1 0 0 1-.25 1z"/></svg>
    01632 960418
  </div>
</header>

<nav class="main-nav">
  <a class="active" href="#">About</a>
  <a href="#">Printing</a>
  <a href="#">Graphic Design</a>
  <a href="#">Web Design</a>
  <a href="#">Art Work Guide</a>
  <a href="#">Sample Pack</a>
  <a href="#">Upload</a>
</nav>

<section class="hero">
  <div class="hero-art" role="img" aria-label="Photo of stacked A6 flyers, paper sheets and coloured pencils"></div>
  <div class="hero-copy">
    <h1>5000 A6 FLYERS</h1>
    <p>Printed on 250 gsm gloss, full color, double sided.</p>
  </div>
  <div class="price-badge"><small>From Just</small><strong>£88</strong></div>
</section>

<section class="promo-strip">
  <div class="promo promo-delivery">
    <h2>FREE DELIVERY</h2>
    <p>All Prices Included</p>
    <div class="van" role="img" aria-label="Illustration of a delivery van"></div>
  </div>
  <div class="promo promo-cards">
    <div class="card-art" role="img" aria-label="Photo of printed business cards"></div>
    <div class="card-copy">
      <h3>Design Your Own <b>Business Card</b></h3>
      <p>Prices start from just £9</p>
      <a class="btn-order" href="#">ORDER NOW ›</a>
    </div>
  </div>
</section>

<section class="popular">
  <aside class="category-list">
    <h2>Popular Products</h2>
    <ul>
      <li class="current">Flyer Printing</li>
      <li>Folded Flyers</li>
      <li>Brochure Printing</li>
      <li>Poster Printing</li>
      <li>Business Cards</li>
      <li>Letterhead Printing</li>
      <li>Compliment Slips</li>
      <li>Rollup Banners</li>
      <li>Invoice Pads &amp; NCR Pads</li>
      <li>Stickers and Labels</li>
      <li>Presentation Folders</li>
      <li>Christmas Cards</li>
    </ul>
  </aside>
  <div class="product-grid">
    <article class="product-card"><div class="product-image" role="img" aria-label="Photo of business cards"></div><h3>Business Card</h3><div class="product-meta">£0.00<a class="btn-shop" href="#">SHOP NOW ›</a></div></article>
    <article class="product-card"><div class="product-image" role="img" aria-label="Photo of A5 flyers"></div><h3>A5 Flyer</h3><div class="product-meta">£0.00<a class="btn-shop" href="#">SHOP NOW ›</a></div></article>
    <article class="product-card"><div class="product-image" role="img" aria-label="Photo of A6 flyers"></div><h3>A6 Flyer</h3><div class="product-meta">£0.00<a class="btn-shop" href="#">SHOP NOW ›</a></div></article>
    <article class="product-card"><div class="product-image" role="img" aria-label="Photo of business cards"></div><h3>Business Card</h3><div class="product-meta">£0.00<a class="btn-shop" href="#">SHOP NOW ›</a></div></article>
    <article class="product-card"><div class="product-image" role="img" aria-label="Photo of A5 flyers"></div><h3>A5 Flyer</h3><div class="product-meta">£0.00<a class="btn-shop" href="#">SHOP NOW ›</a></div></article>
    <article class="product-card"><div class="product-image" role="img" aria-label="Photo of A6 flyers"></div><h3>A6 Flyer</h3><div class="product-meta">£0.00<a class="btn-shop" href="#">SHOP NOW ›</a></div></article>
  </div>
</section>

<section class="portfolio">
  <h2 class="section-title">Sales Our Portfolio</h2>
  <svg class="carousel-arrow prev" viewBox="0 0 20 40"><path d="M16 4 4 20l12 16"/></svg>
  <svg class="carousel-arrow next" viewBox="0 0 20 40"><path d="M4 4l12 16L4 36"/></svg>
  <div class="portfolio-row">
    <div class="portfolio-item"><div class="portfolio-image" role="img" aria-label="Business card design sample"></div><h3>Business Card</h3></div>
    <div class="portfolio-item"><div class="portfolio-image" role="img" aria-label="A5 flyer design sample"></div><h3>A5 Flyer</h3></div>
    <div class="portfolio-item"><div class="portfolio-image" role="img" aria-label="A6 flyer design sample"></div><h3>A6 Flyer</h3></div>
    <div class="portfolio-item"><div class="portfolio-image" role="img" aria-label="Website design sample"></div><h3>Web Design</h3></div>
  </div>
</section>

<section class="latest-news">
  <div class="news-image" role="img" aria-label="Photo of printed expo flyers and leaflets"></div>
  <div class="news-body">
    <h2>North East Expo</h2>
    <div class="news-meta">Posted by Adam Carter on 3rd April 2015 in News</div>
    <p>This week Adam and Lisa attended the North East Expo at Harrowgate Park, the home of the local rugby club. Over 1,000 people attended the event, which saw over 100 companies exhibit their work, and we were proud to print flyers and banners for many of them on the day.</p>
    <a class="read-more" href="#">READ MORE</a>
    <a class="btn-blog" href="#">READ MORE OUR BLOG ›</a>
  </div>
</section>

<section class="offer-band">
  <div class="offer-label">Special offer</div>
  <div class="offer-detail">
    <span class="season">Summer Print Sale</span>
    <div class="deal">15% OFF EVERYTHING <i></i> 2 WEEKS ONLY</div>
  </div>
</section>

<footer class="site-footer">
  <div class="footer-links">
    <h3>Useful Links</h3>
    <ul>
      <li>Special Offers</li>
      <li>Terms and Conditions</li>
      <li>Privacy Policy</li>
      <li>Trade Account</li>
    </ul>
  </div>
  <div class="footer-contact">
    <h3>Get In Touch With Us</h3>
    <div class="contact-line"><svg viewBox="0 0 10 10"><rect x="1" y="1" width="8" height="8"/></svg>Zoravquill.com Limited</div>
    <div class="contact-line"><svg viewBox="0 0 10 10"><path d="M5 0a3.5 3.5 0 0 1 3.5 3.5C8.5 6 5 10 5 10S1.5 6 1.5 3.5A3.5 3.5 0 0 1 5 0z"/></svg>Unit 4, Fernlow Trade Park, Ashby Vale, County Elmford, EF9 7RL</div>
    <div class="contact-line"><svg viewBox="0 0 10 10"><path d="M2 0h2l1 3-1.5 1a6 6 0 0 0 2.5 2.5L7 5l3 1v2a2 2 0 0 1-2 2A8 8 0 0 1 0 2a2 2 0 0 1 2-2z"/></svg>01632 960418</div>
    <div class="contact-line"><svg viewBox="0 0 10 10"><path d="M0 2h10v6H0zM0 2l5 3.5L10 2" /></svg>hello@zoravquill.com</div>
  </div>
  <div class="footer-payment">
    <h3>Payment Gateway</h3>
    <div class="payment-row" aria-label="Accepted payment methods">
      <span></span><span></span><span></span><span></span><span></span><span></span><span></span>
    </div>
  </div>
</footer>

<div class="legal-bar">
  Registered in England and Wales. Company registration number 0000000. VAT registration number 000000000.<br>
  Zoravquill.com Limited, Unit 4, Fernlow Trade Park, Ashby Vale, County Elmford, EF9 7RL
</div>

</body>
</html>
```